PowerPoint Template Needed for Investment Firm

Norvelle Capital Management is an emerging wealth management firm based in New Jersey. It offers superior investment returns to high net worth individuals and institutions by finding undervalued assets.

We recently selected a company logo which was inspired by the Tucana constellation. Beta Tucanae is a group of six stars, containing star cluster 47 Tucanae, rated the second brightest object in the sky.

Now we need a PowerPoint template with the designs for the following:

1. Title/cover page slide
2. Content slide with title
3. Section slide - to introduce a new section
4. Final slide - with contact information

The slides will be used at investor presentations, that is, to provide information about the company to potential investors. Since we are an investment firm, the design should project a sense of stability, growth and professionalism. The owner is interested in something simple yet striking, which of course is consistent with the logo. I'm thinking more conservative colors and Sans Serif fonts.

I plan on changing the status to non-refundable once I see some designs that I really like.

Target Market(s)

Wealthy individuals, probably middle aged or older, in the US

Industry/Entity Type

Conservative

Requirements
Must have
• Sans serif fonts
Clean, very professional look
Conservative colors that complement existing logo
Should not have
• Anything too busy or complicated

```html
<!DOCTYPE html>
<html lang="en">
<head>
<meta charset="utf-8">
<title>Section Slide</title>
<link rel="stylesheet" href="https://fonts.googleapis.com/css2?family=Arimo:wght@400&display=swap">
<style>
  :root {
    --frame-blue: #0d3dae;
    --accent-blue: #0e3fb0;
    --title-navy: #0b1870;
    --slide-white: #ffffff;
    --guide-grey: #555555;
    --number-ink: #222222;
  }
  html, body {
    margin: 0;
    padding: 0;
    width: 1200px;
    height: 902px;
    overflow: hidden;
    background: var(--frame-blue);
  }
  .slide {
    position: relative;
    width: 1200px;
    height: 902px;
    background: var(--frame-blue);
    font-family: "Arimo", Arial, sans-serif;
  }
  .slide-panel {
    position: absolute;
    left: 19px;
    top: 27px;
    width: 1162px;
    height: 847px;
    background: var(--slide-white);
    border-radius: 15px;
  }
  .header-graphic {
    position: absolute;
    left: 0;
    top: 0;
  }
  .section-title-box {
    position: absolute;
    left: 40px;
    top: 281px;
    width: 1113px;
    height: 72px;
    border: 1px dotted var(--guide-grey);
    box-sizing: border-box;
    display: flex;
    align-items: center;
  }
  .section-title {
    margin: 0;
    padding-left: 1px;
    font-size: 60px;
    font-weight: 400;
    letter-spacing: -2px;
    color: var(--title-navy);
    line-height: 1;
    -webkit-text-stroke: 0.6px var(--title-navy);
  }
  .slide-number {
    position: absolute;
    right: 41px;
    top: 836px;
    font-size: 20px;
    font-weight: 400;
    color: var(--number-ink);
  }
</style>
</head>
<body>
  <div class="slide">
    <div class="slide-panel"></div>
    <svg class="header-graphic" width="1200" height="902" viewBox="0 0 1200 902" aria-hidden="true">
      <rect class="header-rule" x="42" y="249" width="990" height="6" fill="var(--accent-blue)"/>
      <polygon class="chevron" points="1016,144 1066,144 1109,200 1066,256 1016,256 1059,200" fill="var(--accent-blue)"/>
      <polygon class="chevron" points="1084,144 1129,144 1172,200 1129,256 1084,256 1127,200" fill="var(--accent-blue)"/>
    </svg>
    <div class="section-title-box">
      <h1 class="section-title">Section title</h1>
    </div>
    <div class="slide-number">3</div>
  </div>
</body>
</html>
```